Flyer-Design für Babyfotograf
grinsi77 ist auf alle meine Wünsche eingegangen und hat das Layout sehr gut umgesetzt. Vielen Dank für die gute und reibungslose Zusammenarbeit.
Zielgruppe
Als Fotograf bin ich spezialisiert auf Babybauch- und Neugeborenenshootings, meine Zielgruppe sind daher schwangere Frauen und Familien die bald / vor kurzem Nachwuchs erwartet haben.
Neben den beiden sparten biete ich noch Baby- und Familienshootings an.
Aufgabenstellung
Ich hätte gerne einen besonderen Flyer, ein Faltspiel.
Die Lieferung der fertigen Datei bitte als offene Indesign 5.5 Datei, falls mal Änderungen anstehen und als druckfertige Datei im PDF Format.
Das Datenblatt der Druckerei finden Sie hier:
http://www.kammerl-satz.de/Papierwelt-Laden/PDF-Vorlagen/Vorlage_Endlosfaltkarte_DL.pdf
In der Anlage bekommen Sie einige Infos rund um meine Dienstleistungen, es wäre toll wenn diese textlich ggf. noch besser angepasst werden auf den Kundennutzen und die Vorteile welche der Kunde hat.
Ich hab mal noch einen Flyer beigefügt um mein corporate design zu erkennen.

```html
<!DOCTYPE html>
<html lang="de">
<head>
<meta charset="utf-8">
<title>Faltflyer Babyfotografie – Jonas Albrecht</title>
<link rel="stylesheet" href="https://fonts.googleapis.com/css2?family=Lobster&family=Merriweather:wght@400;700&display=swap">
<style>
:root{
  --stage:#434343;
  --red:#9b3326;
  --beige:#e3ddd3;
  --beige-light:#f1ede6;
  --beige-mid:#d8d0c3;
  --paper:#ffffff;
  --ink:#555049;
  --guide-pink:#e2679a;
  --guide-blue:#4fb3e6;
  --band-red:#e0111b;
  --band-orange:#f08c00;
}
*{margin:0;padding:0;box-sizing:border-box}
html,body{width:730px;height:1200px;overflow:hidden;background:var(--stage)}
body{position:relative;font-family:"Merriweather",Georgia,serif;color:var(--ink)}
.abs{position:absolute}
.script{font-family:"Lobster",cursive;color:var(--red);font-weight:400}

/* ornamental background area, rendered as soft tonal field */
.ornament-field{
  position:absolute;inset:0;
  background:
    radial-gradient(ellipse 40% 55% at 18% 30%, var(--beige-light) 0%, rgba(241,237,230,0) 70%),
    radial-gradient(ellipse 35% 50% at 82% 70%, var(--beige-light) 0%, rgba(241,237,230,0) 70%),
    radial-gradient(ellipse 30% 45% at 50% 100%, var(--beige-light) 0%, rgba(241,237,230,0) 70%),
    linear-gradient(135deg, #e7e1d7 0%, var(--beige-mid) 50%, #e6e0d6 100%);
}

/* rows */
.thumb{position:absolute;left:11px;width:160px;height:80px;background:var(--beige);overflow:hidden}
.panel{position:absolute;left:182px;width:532px;height:266px;background:var(--beige);overflow:hidden}
.row1{top:27px}.row2{top:319px}.row3{top:611px}.row4{top:903px}

.photo{position:absolute;box-shadow:0 1px 3px rgba(0,0,0,.35)}
.photo-warm{background:linear-gradient(135deg,#b99a84,#7a6253)}
.photo-skin{background:linear-gradient(135deg,#e9c9b8,#c99a86)}
.photo-park{background:linear-gradient(180deg,#8f9a78,#5f6b45 60%,#9a8a6a)}
.photo-dark{background:linear-gradient(135deg,#3b3b3b,#1e1e1e)}
.photo-sun{background:linear-gradient(180deg,#d9c69a,#8b9a5a 55%,#7a8c4a)}
.photo-grey{background:linear-gradient(135deg,#8a8a8a,#3e3e3e)}
.photo-wood{background:linear-gradient(180deg,#7b6a5e,#a28f80 60%,#8d7e73)}

/* brand circle */
.brand{position:absolute;border-radius:50%;background:var(--red);color:#fff;display:flex;flex-direction:column;align-items:center;justify-content:center;text-align:center;font-family:"Merriweather",Georgia,serif;font-weight:400}
.brand .name{letter-spacing:.12em;text-transform:uppercase}
.brand .domain{letter-spacing:.06em}

/* panel 1 */
.p1-title{left:13px;top:12px;white-space:nowrap}
.p1-title .small{font-size:20px}
.p1-title .big{font-size:36px}
.p1-brand{left:309px;top:22px;width:170px;height:170px}
.p1-brand .name{font-size:9px}
.p1-brand .domain{font-size:7px;margin-top:4px}
.p1-claim{left:371px;top:206px;font-size:21px;line-height:28px}

/* panel 2 */
.p2-head{left:0;width:532px;text-align:center}
.p2-head1{top:6px;font-size:22px}
.p2-head2{top:34px;font-size:24px}
.p2-pair{left:142px;top:68px;width:243px;height:78px;transform:rotate(-1.5deg);display:flex}
.p2-pair div{flex:1}
.p2-text{left:146px;top:146px;width:241px;height:108px;background:var(--paper);padding:11px 10px 0 10px;font-size:8px;line-height:10.8px}
.p2-text p+p{margin-top:5px}

/* panel 3 */
.p3{background:var(--paper)}
.p3-back{left:133px;top:0;width:266px;height:266px;overflow:hidden}
.p3-top{left:169px;top:3px;width:204px;height:126px;transform:rotate(2deg)}
.p3-feet{left:150px;top:134px;width:129px;height:131px;transform:rotate(-1deg)}
.p3-card{left:277px;top:153px;width:122px;height:113px;background:var(--paper);padding:7px 8px}
.p3-studio{font-size:8.4px;font-weight:700;color:var(--red);line-height:11px}
.p3-contact{list-style:none;margin-top:6px;font-size:5.6px;line-height:7.6px}
.p3-contact li{display:flex;gap:4px;margin-bottom:2.4px;align-items:flex-start}
.p3-contact svg{flex:none;width:7px;height:7px;fill:var(--red)}
.p3-brand{left:309px;top:84px;width:86px;height:86px}
.p3-brand .name{font-size:4.6px}
.p3-brand .domain{font-size:3.8px;margin-top:2px}

/* panel 4 */
.p4-head{left:130px;width:272px;text-align:center;top:6px;font-size:24px;line-height:29px}
.reasons{position:absolute;font-size:5.5px;line-height:7.6px;overflow:hidden}
.reasons p{margin-bottom:3.4px}
.reasons b{font-family:"Lobster",cursive;font-weight:400;color:var(--red);font-size:6.6px}
.r-left{left:10px;top:10px;width:113px;height:250px;background:var(--paper);padding:6px 8px}
.r-mid-a{left:143px;top:66px;width:123px;height:193px;background:var(--paper);padding:6px 6px}
.r-mid-b{left:266px;top:66px;width:123px;height:193px;background:var(--paper);padding:6px 6px}
.r-right{left:416px;top:10px;width:108px;height:200px}
.p4-brand{left:443px;top:192px;width:86px;height:86px}
.p4-brand .name{font-size:4.6px}
.p4-brand .domain{font-size:3.8px;margin-top:2px}

/* thumbnails */
.guide{position:absolute;background:var(--guide-pink)}
.guide.v{width:1px;top:0;height:80px}
.guide.h{height:0;left:0;width:160px;border-top:1px dashed var(--guide-blue);background:none}
.tiny{font-size:2.4px;line-height:3.2px}
.band{position:absolute;width:40px;display:flex;align-items:center;justify-content:center;text-align:center;font-size:2.6px;line-height:3.2px;font-weight:700;color:#5a1a10;padding:2px}
</style>
</head>
<body>

<!-- Row 1: title panel -->
<section class="thumb row1" aria-label="Vorschau Titelseite">
  <div class="ornament-field" role="img" aria-label="Ornamentales Rankenmuster in Beige"></div>
  <div class="photo photo-wood" role="img" aria-label="Foto: schlafendes Neugeborenes in einer Holzkiste" style="left:0;top:15px;width:105px;height:65px;clip-path:polygon(0 28%,100% 0,100% 100%,0 100%);box-shadow:none"></div>
  <div class="script abs" style="left:4px;top:3px;font-size:9px;white-space:nowrap">Es gibt Momente,</div>
  <div class="brand" style="left:93px;top:7px;width:50px;height:50px"><span class="name" style="font-size:2.8px">Jonas Albrecht</span><span class="domain" style="font-size:2.2px;margin-top:1px">babyfoto-musterstadt.de</span></div>
  <div class="script abs" style="left:111px;top:61px;font-size:6.4px;line-height:8px">die kommen<br>nie wieder…</div>
  <div class="guide v" style="left:79px"></div>
  <div class="guide h" style="top:19px"></div>
  <div class="guide h" style="top:61px"></div>
</section>

<section class="panel row1" aria-label="Titelseite">
  <div class="ornament-field" role="img" aria-label="Ornamentales Rankenmuster in Beige und Weiß"></div>
  <div class="photo photo-wood" role="img" aria-label="Foto: schlafendes Neugeborenes bäuchlings auf Fell in einer alten Holzkiste" style="left:0;top:50px;width:350px;height:216px;clip-path:polygon(0 28%,100% 0,100% 100%,0 100%);box-shadow:none"></div>
  <h1 class="script abs p1-title"><span class="small">Es gibt</span> <span class="big">Momente,</span></h1>
  <div class="brand p1-brand"><span class="name">Jonas Albrecht</span><span class="domain">babyfoto-musterstadt.de</span></div>
  <p class="script abs p1-claim">die kommen<br>nie wieder…</p>
</section>

<!-- Row 2: inner spread -->
<section class="thumb row2" aria-label="Vorschau Innenseite">
  <div class="ornament-field" role="img" aria-label="Ornamentales Rankenmuster in Beige"></div>
  <div class="photo photo-skin" role="img" aria-label="Foto: Babybauch" style="left:8px;top:2px;width:24px;height:16px"></div>
  <div class="photo photo-park" role="img" aria-label="Foto: Schwangere im Park" style="left:2px;top:23px;width:35px;height:36px"></div>
  <div class="photo photo-skin" role="img" aria-label="Foto: schlafendes Baby" style="left:8px;top:63px;width:24px;height:16px"></div>
  <div class="script abs" style="left:40px;top:1px;width:80px;text-align:center;font-size:6.2px;line-height:8px">… wie die ersten<br>Lebenstage eures Babys!</div>
  <div class="photo photo-skin" role="img" aria-label="Foto: Neugeborenes" style="left:43px;top:20px;width:37px;height:23px"></div>
  <div class="photo photo-dark" role="img" aria-label="Foto: Schwangere mit Kind" style="left:80px;top:20px;width:37px;height:23px"></div>
  <div class="abs tiny" style="left:46px;top:47px;width:70px;background:#fff;padding:2px;height:30px">Kurzer Einleitungstext über Babybauch und erste Lebenstage.</div>
  <div class="photo photo-warm" role="img" aria-label="Foto: Baby mit Mütze" style="left:128px;top:2px;width:24px;height:16px"></div>
  <div class="photo photo-sun" role="img" aria-label="Foto: Paar auf der Wiese" style="left:123px;top:23px;width:35px;height:36px"></div>
  <div class="photo photo-grey" role="img" aria-label="Foto: Familie in Schwarzweiß" style="left:128px;top:63px;width:24px;height:16px"></div>
  <div class="guide v" style="left:38px"></div>
  <div class="guide v" style="left:121px"></div>
</section>

<section class="panel row2" aria-label="Innenseite">
  <div class="ornament-field" role="img" aria-label="Ornamentales Rankenmuster in Beige und Weiß"></div>
  <div class="photo photo-skin" role="img" aria-label="Foto: Hände auf einem Babybauch" style="left:26px;top:7px;width:80px;height:53px"></div>
  <div class="photo photo-park" role="img" aria-label="Foto: Schwangere Frau im herbstlichen Park" style="left:8px;top:75px;width:115px;height:118px"></div>
  <div class="photo photo-skin" role="img" aria-label="Foto: schlafendes Neugeborenes auf Decke" style="left:26px;top:206px;width:80px;height:53px"></div>
  <h2 class="script abs p2-head p2-head1">… wie die ersten</h2>
  <h2 class="script abs p2-head p2-head2">Lebenstage eures Babys!</h2>
  <div class="abs p2-pair">
    <div class="photo-skin" role="img" aria-label="Foto: Neugeborenes auf hellem Fell"></div>
    <div class="photo-dark" role="img" aria-label="Foto: Schwangere mit Kleinkind vor dunklem Hintergrund"></div>
  </div>
  <div class="abs p2-text">
    <p>Das letzte Drittel der Schwangerschaft, eine spannende Zeit. Der Babybauch wird immer größer, runder und die Freude, Euer Baby in den Händen zu halten wächst jeden Tag.</p>
    <p>Als Fotograf bin ich auf die <b>Schwangerschaft- und Neugeborenenfotografie</b> spezialisiert und halte Euch diese so wertvollen Momente für immer fest.</p>
  </div>
  <div class="photo photo-warm" role="img" aria-label="Foto: Neugeborenes mit Bärenmütze" style="left:427px;top:7px;width:79px;height:53px"></div>
  <div class="photo photo-sun" role="img" aria-label="Foto: werdende Eltern auf einer Wiese im Abendlicht" style="left:408px;top:75px;width:114px;height:117px"></div>
  <div class="photo photo-grey" role="img" aria-label="Foto: Familie mit Baby in Schwarzweiß" style="left:427px;top:206px;width:79px;height:53px"></div>
</section>

<!-- Row 3: back panel -->
<section class="thumb row3" aria-label="Vorschau Rückseite" style="width:161px;background:#fff">
  <div class="band" style="left:0;top:0;height:20px;background:var(--band-red)">Dieser Bereich nicht gestalten</div>
  <div class="band" style="left:0;top:20px;height:40px;background:var(--band-orange)">Dieser Bereich wird vom 1. Knick übernommen</div>
  <div class="band" style="left:0;top:60px;height:20px;background:var(--band-red)">Dieser Bereich nicht gestalten</div>
  <div class="abs" style="left:40px;top:0;width:81px;height:80px;overflow:hidden"><div class="ornament-field" role="img" aria-label="Ornamentales Rankenmuster in Beige"></div></div>
  <div class="photo photo-warm" role="img" aria-label="Foto: Neugeborenes" style="left:50px;top:1px;width:62px;height:38px"></div>
  <div class="photo photo-skin" role="img" aria-label="Foto: Babyfüße" style="left:45px;top:40px;width:39px;height:40px"></div>
  <div class="abs" style="left:85px;top:50px;width:36px;height:30px;background:#fff;padding:2px;font-size:2.6px;line-height:3.2px;color:var(--red);font-weight:700">Fotostudio<br>Jonas Albrecht</div>
  <div class="brand" style="left:94px;top:25px;width:26px;height:26px"><span class="name" style="font-size:1.6px">Jonas Albrecht</span></div>
  <div class="band" style="left:121px;top:0;height:20px;background:var(--band-red)">Dieser Bereich nicht gestalten</div>
  <div class="band" style="left:121px;top:20px;height:40px;background:var(--band-orange)">Dieser Bereich wird vom 1. Knick übernommen</div>
  <div class="band" style="left:121px;top:60px;height:20px;background:var(--band-red)">Dieser Bereich nicht gestalten</div>
</section>

<section class="panel row3 p3" aria-label="Rückseite mit Kontakt">
  <div class="abs p3-back"><div class="ornament-field" role="img" aria-label="Ornamentales Rankenmuster in Beige und Weiß"></div></div>
  <div class="photo photo-warm p3-top" role="img" aria-label="Foto: schlafendes Neugeborenes in einem Korb mit grauer Decke"></div>
  <div class="photo photo-skin p3-feet" role="img" aria-label="Foto: Babyfüße auf hellem Fell"></div>
  <div class="abs p3-card">
    <h3 class="p3-studio">Fotostudio<br>Jonas Albrecht</h3>
    <ul class="p3-contact">
      <li><svg viewBox="0 0 10 10"><path d="M5 0a3.4 3.4 0 0 0-3.4 3.4C1.6 6 5 10 5 10s3.4-4 3.4-6.6A3.4 3.4 0 0 0 5 0zm0 4.8a1.4 1.4 0 1 1 0-2.8 1.4 1.4 0 0 1 0 2.8z"/></svg><span>Lindenweg 4<br>73999 Wiesental</span></li>
      <li><svg viewBox="0 0 10 10"><path d="M2.2 0.4l1.6 2.2-1 1.1c.6 1.4 1.6 2.4 3 3l1.1-1 2.2 1.6-.8 1.9C4.6 9.2.8 5.4.3 1.2z"/></svg><span>(0 71 11) 23 45 678</span></li>
      <li><svg viewBox="0 0 10 10"><path d="M0 2h10v6H0zm1 .8v.3l4 2.6 4-2.6v-.3z"/></svg><span>jonas@babyfoto-musterstadt.de</span></li>
      <li><svg viewBox="0 0 10 10"><path d="M0 1h10v6.5H6v1h1.5V9.5h-5V8.5H4v-1H0zm1 1v4.5h8V2z"/></svg><span>www.babyfoto-musterstadt.de</span></li>
      <li><svg viewBox="0 0 10 10"><rect x="0.5" y="0.5" width="9" height="9" rx="1"/></svg><span>babyfoto.musterstadt</span></li>
    </ul>
  </div>
  <div class="brand p3-brand"><span class="name">Jonas Albrecht</span><span class="domain">babyfoto-musterstadt.de</span></div>
</section>

<!-- Row 4: reasons -->
<section class="thumb row4" aria-label="Vorschau 31 Gründe" style="width:161px">
  <div class="ornament-field" role="img" aria-label="Ornamentales Rankenmuster in Beige"></div>
  <div class="abs tiny" style="left:3px;top:3px;width:34px;height:74px;background:#fff;padding:2px">Gründe in Kurzform</div>
  <div class="script abs" style="left:40px;top:2px;width:80px;text-align:center;font-size:6.4px;line-height:8px">31 gute Gründe für<br>ein Shooting mit mir…</div>
  <div class="abs tiny" style="left:44px;top:21px;width:74px;height:56px;background:#fff;padding:2px">Gründe in Kurzform</div>
  <div class="abs tiny" style="left:124px;top:3px;width:34px">Gründe in Kurzform</div>
  <div class="brand" style="left:134px;top:57px;width:26px;height:26px"><span class="name" style="font-size:1.6px">Jonas Albrecht</span></div>
  <div class="guide v" style="left:40px"></div>
  <div class="guide v" style="left:121px"></div>
</section>

<section class="panel row4" aria-label="31 gute Gründe">
  <div class="ornament-field" role="img" aria-label="Ornamentales Rankenmuster in Beige und Weiß"></div>
  <h2 class="script abs p4-head">31 gute Gründe für<br>ein Shooting mit mir…</h2>
  <div class="reasons r-left">
    <p><b>1&nbsp; Fotos als jpg-Datei</b></p>
    <p><b>2&nbsp; Erfahrung:</b> Seit 2010 habe ich mich auf die Fotografie von Schwangeren &amp; Neugeborenen spezialisiert.</p>
    <p><b>3&nbsp; Parkplatz am Studio</b></p>
    <p><b>4&nbsp; Spielekiste für die „Großen“:</b> Damit für die Geschwisterkinder keine Langeweile aufkommt.</p>
    <p><b>5&nbsp; Sicherheit ist das A&amp;O:</b> Ich fotografiere nur in Posen in denen das Baby in dem Moment auch sicher ist.</p>
    <p><b>6&nbsp; Windeln &amp; Hygieneprodukte:</b> Spart Euch das Schleppen, wir haben im Studio alles kostenfrei zur Verfügung.</p>
    <p><b>7&nbsp; Kostenloses WLAN</b></p>
    <p><b>8&nbsp; Requisitenauswahl:</b> Große Auswahl an Decken, Tüchern, Mützchen etc.</p>
    <p><b>9&nbsp; Bequeme Fotoauswahl Zuhause:</b> Über eine kennwortgeschützte Galerie könnt ihr Eure Fotos anschauen.</p>
    <p><b>10&nbsp; Gemütlicher Stillbereich:</b> Für die kleine Trinkpause zwischendurch.</p>
  </div>
  <div class="reasons r-mid-a">
    <p><b>11&nbsp; Babybauchkleider:</b> Mein Fundus an Babybauchkleidern bietet sicherlich auch für Dich das passende.</p>
    <p><b>12&nbsp; Spezialisiert:</b> Auf Schwangere, Neugeborene, Babys &amp; Familien.</p>
    <p><b>13&nbsp; Individuelle Shootings:</b> Auf Eure Wünsche &amp; Vorstellungen angepasst.</p>
    <p><b>14&nbsp; Flexibel:</b> Die Shootings können an einem Ort nach Eurer Wahl statt finden.</p>
    <p><b>15&nbsp; Kurze Bearbeitungszeiten:</b> Wir stellen euch die Fotos innerhalb von 5 Werktagen fix und fertig zur Verfügung.</p>
    <p><b>16&nbsp; Sofort verfügbare Bilder:</b> Nach Bestellung Zahlung könnt ihr auf die Bilder per Download sofort zugreifen.</p>
    <p><b>17&nbsp; Erste-Hilfe:</b> Ich frische mein Wissen im Bereich Erste Hilfe regelmäßig auf, speziell für den Kleinkind und Säuglingsbereich.</p>
  </div>
  <div class="reasons r-mid-b">
    <p><b>18&nbsp; Autobahnnah:</b> Nur 15 Minuten von der Autobahnausfahrt Wiesental Nord.</p>
    <p><b>19&nbsp; Angebote:</b> Durch regelmäßige Aktionen spart ihr Geld.</p>
    <p><b>20&nbsp; Diskretion:</b> Freigaben und Veröffentlichungen werden immer vorher abgesprochen.</p>
    <p><b>21&nbsp; 100% Ausführung:</b> auch im Krankheitsfall</p>
    <p><b>22&nbsp; Referenzen:</b> Viele Babys, Babybäuche und Familien durfte ich bereits fotografieren.</p>
    <p><b>23&nbsp; Geduld:</b> Ich nehme mir Zeit und Geduld die Euer Baby braucht.</p>
    <p><b>24&nbsp; Regelmäßig neue Fotos:</b> Mit dem Babypass begleite ich Euch vom Babybauch über das Neugeborenenshooting bis zum 3. Lebensjahr.</p>
  </div>
  <div class="reasons r-right">
    <p><b>25&nbsp; Abendshooting:</b> Papa ist tagsüber bei der Arbeit? Gerne finden Shootings auch am Abend statt.</p>
    <p><b>26&nbsp; Zufriedenheit:</b> Sollte euer Kind mal keine Lust auf ein Shooting haben, vereinbaren wir einfach einen neuen Termin.</p>
    <p><b>27&nbsp; Empfehlungen:</b> Ihr benötigt Geburtstagskarten oder Wandbilder? Wir geben gerne Empfehlungen ab.</p>
    <p><b>28&nbsp; Auf dem neuesten Stand:</b> Equipement wird regelmäßig gewartet und neue Requisiten sorgen für Abwechslung.</p>
    <p><b>29&nbsp; EC Zahlung</b></p>
    <p><b>30&nbsp; Hochwertige Produkte:</b> Bei den Requisiten lege ich viel Wert auf natürliche und hochwertige Ware.</p>
    <p><b>31&nbsp; Getränke:</b> Kaffee, Tee und Mineralwasser stehen euch kostenfrei zur Verfügung.</p>
  </div>
  <div class="brand p4-brand"><span class="name">Jonas Albrecht</span><span class="domain">babyfoto-musterstadt.de</span></div>
</section>

</body>
</html>
```